School Learner profile graphic representation

I have a set of ideas around communicating our school 'learner profile'. These represent the attitudes, habits and dispositions we are trying to develop through our curriculum and wider enrichment programme. I want the links between the ideas and concepts to be represented in some form of an inforgraphic which can be published and displayed for the whole community to connect with. we run two schools and want the profile to represent for both.

Target Market(s)

Students, Parents, Teachers, Wider community in education

Industry/Entity Type

Education

Font styles to use
Other font styles liked:
• Johnson p22

Colors

Designer to choose colors to be used in the design.

Requirements
Must have
• See my diagram in the ppt.
• The statements Aspiration, Agency, Agility, Altitude with the supporting descriptions. Ideally the values in the center is also represented. The two school logos should also be present somehow (both emblems at least). Let me know if the full logo files are required
Nice to have
• the numbering shown in my diagram is not absolutely necessary is it is not necessarily a linear process and rather cyclical and cross reinforcing

```html
<!DOCTYPE html>
<html lang="en">
<head>
<meta charset="utf-8">
<title>Envisioning Our Learners</title>
<link href="https://fonts.googleapis.com/css2?family=Kanit:wght@300;400;500&display=swap" rel="stylesheet">
<style>
  :root {
    --red: #e61e2a;
    --red-deep: #8c0a10;
    --maroon: #7a0f14;
    --pink: #f27a7f;
    --ink: #111111;
    --white: #ffffff;
    --ring-dark: #231f20;
    --grey: #d9d9d9;
  }
  html, body { margin: 0; padding: 0; overflow: hidden; }
  .canvas {
    position: relative;
    width: 1050px;
    height: 1200px;
    overflow: hidden;
    background:
      linear-gradient(135deg, transparent 55%, rgba(90,0,5,.45) 55%, rgba(90,0,5,.45) 70%, transparent 70%),
      linear-gradient(35deg, rgba(60,0,0,.35) 0 20%, transparent 20% 80%, rgba(60,0,0,.3) 80%),
      linear-gradient(160deg, #b3121b, #d8141f 40%, #8e0b12);
  }
  .panel {
    position: absolute;
    left: 36px; top: 35px;
    width: 979px; height: 1131px;
    background: var(--white);
  }
  .art { position: absolute; inset: 0; }
  .title { font-family: "Kanit", sans-serif; font-weight: 500; font-size: 68px; fill: var(--ink); }
  .heading { font-family: "Kanit", sans-serif; font-weight: 400; font-size: 23px; fill: var(--red); }
  .body { font-family: "Kanit", sans-serif; font-weight: 300; font-size: 18.5px; fill: var(--ink); }
  .ring-label { font-family: "Kanit", sans-serif; font-weight: 500; font-size: 28px; fill: var(--white); }
  .value { font-family: "Kanit", sans-serif; font-weight: 400; font-size: 17px; fill: var(--ink); }
  .school-name { font-family: "Kanit", sans-serif; font-weight: 400; font-size: 13px; fill: var(--red); }
</style>
</head>
<body>
<div class="canvas">
  <div class="panel"></div>
  <svg class="art" width="1050" height="1200" viewBox="0 0 1050 1200" xmlns="http://www.w3.org/2000/svg">
    <defs>
      <linearGradient id="sky-mountain" x1="0" y1="0" x2="0" y2="1">
        <stop offset="0" stop-color="#e8f3f8"/><stop offset=".45" stop-color="#2aa5c8"/><stop offset="1" stop-color="#5b4fa3"/>
      </linearGradient>
      <linearGradient id="target-scene" x1="0" y1="0" x2="1" y2="1">
        <stop offset="0" stop-color="#2e6fb5"/><stop offset="1" stop-color="#3fa6ef"/>
      </linearGradient>
      <radialGradient id="podium-scene">
        <stop offset="0" stop-color="#7d73c4"/><stop offset=".65" stop-color="#5a52a8"/><stop offset=".66" stop-color="#ffffff"/>
      </radialGradient>
      <linearGradient id="flight-scene" x1="0" y1="0" x2="0" y2="1">
        <stop offset="0" stop-color="#5cc4f5"/><stop offset="1" stop-color="#bfe9fb"/>
      </linearGradient>
      <radialGradient id="compass-face">
        <stop offset="0" stop-color="#ffffff"/><stop offset=".7" stop-color="#e6e9f0"/><stop offset="1" stop-color="#2f3f66"/>
      </radialGradient>
      <path id="arc-attitude" d="M 399.1 674.2 A 135 135 0 0 1 561 497.6" fill="none"/>
      <path id="arc-mind" d="M 606.3 513.3 A 140 140 0 0 1 663.9 652.3" fill="none"/>
    </defs>

    <text class="title" x="525" y="115" text-anchor="middle">Envisioning Our Learners</text>

    <!-- Altitude -->
    <text class="heading" x="531" y="164" text-anchor="middle">Learners with Altitude:</text>
    <text class="body" x="529" y="190" text-anchor="middle">Achieve great things and</text>
    <text class="body" x="531" y="216" text-anchor="middle">work to elevate others</text>
    <circle cx="527" cy="322" r="85" fill="url(#sky-mountain)" role="img" aria-label="Illustration of a climber planting a flag on a mountain summit"/>
    <circle cx="527" cy="322" r="85" fill="none" stroke="var(--ring-dark)" stroke-width="9"/>

    <!-- Connectors -->
    <line x1="298" y1="634" x2="332" y2="634" stroke="var(--red)" stroke-width="2.5"/>
    <circle cx="298" cy="634" r="4" fill="var(--red)"/>
    <line x1="720" y1="630" x2="752" y2="630" stroke="var(--maroon)" stroke-width="2.5"/>
    <circle cx="752" cy="630" r="4" fill="var(--maroon)"/>
    <line x1="520" y1="822" x2="520" y2="855" stroke="var(--pink)" stroke-width="2.5"/>
    <circle cx="520" cy="855" r="4" fill="var(--pink)"/>

    <!-- Central ring -->
    <circle cx="526" cy="628" r="155" fill="none" stroke="var(--pink)" stroke-width="79"/>
    <path d="M 407.3 727.7 A 155 155 0 0 1 579 482.3" fill="none" stroke="var(--red)" stroke-width="79" stroke-linecap="round"/>
    <path d="M 579 482.3 A 155 155 0 0 1 644.7 727.7" fill="none" stroke="var(--maroon)" stroke-width="79" stroke-linecap="round"/>
    <path d="M 644.7 727.7 A 155 155 0 0 1 610 758" fill="none" stroke="var(--pink)" stroke-width="79" stroke-linecap="round"/>

    <text class="ring-label"><textPath href="#arc-attitude">Attitude &amp; Spirit</textPath></text>
    <text class="ring-label"><textPath href="#arc-mind" startOffset="15">Mind</textPath></text>
    <text class="ring-label" x="518" y="790" text-anchor="middle" transform="rotate(4 518 780)">Heart</text>
    <path d="M583 789 c-6 -6 -14 -12 -14 -19 a7 7 0 0 1 14 -3 a7 7 0 0 1 14 3 c0 7 -8 13 -14 19 z" fill="var(--white)"/>

    <circle cx="526" cy="628" r="117" fill="var(--white)"/>
    <circle cx="526" cy="628" r="111" fill="none" stroke="var(--grey)" stroke-width="5"/>
    <circle cx="526" cy="628" r="104" fill="var(--white)" stroke="var(--ring-dark)" stroke-width="8"/>
    <circle cx="526" cy="628" r="60" fill="url(#compass-face)" role="img" aria-label="Compass rose with cardinal points"/>
    <text class="value" x="525" y="547" text-anchor="middle">Values</text>
    <text class="value" x="447" y="630" text-anchor="middle" transform="rotate(-90 447 630)">Ethics</text>
    <text class="value" x="604" y="630" text-anchor="middle" transform="rotate(90 604 630)">Morals</text>
    <text class="value" x="530" y="717" text-anchor="middle" transform="rotate(-6 530 712)">Principles</text>

    <!-- Agility -->
    <circle cx="197" cy="630" r="85" fill="url(#target-scene)" role="img" aria-label="Illustration of a learner leaping towards a target"/>
    <circle cx="197" cy="630" r="85" fill="none" stroke="var(--ring-dark)" stroke-width="9"/>
    <text class="heading" x="191" y="747" text-anchor="middle">Learners with Agility</text>
    <text class="body" x="191" y="772" text-anchor="middle">Are determined,</text>
    <text class="body" x="191" y="798" text-anchor="middle">equipped and</text>
    <text class="body" x="188" y="824" text-anchor="middle">able to accomplish</text>
    <text class="body" x="191" y="850" text-anchor="middle">great things</text>

    <!-- Agency -->
    <circle cx="853" cy="628" r="85" fill="url(#podium-scene)" role="img" aria-label="Illustration of a learner on a podium raising a trophy"/>
    <circle cx="853" cy="628" r="85" fill="none" stroke="var(--ring-dark)" stroke-width="9"/>
    <text class="heading" x="856" y="745" text-anchor="middle">Learners with Agency</text>
    <text class="body" x="853" y="770" text-anchor="middle">Believe in their</text>
    <text class="body" x="855" y="796" text-anchor="middle">capacity and</text>
    <text class="body" x="853" y="822" text-anchor="middle">responsibility to</text>
    <text class="body" x="856" y="848" text-anchor="middle">do great things</text>

    <!-- Aspiration -->
    <circle cx="520" cy="961" r="85" fill="url(#flight-scene)" role="img" aria-label="Illustration of a learner flying upward with a jetpack through clouds"/>
    <circle cx="520" cy="961" r="85" fill="none" stroke="var(--ring-dark)" stroke-width="9"/>
    <text class="heading" x="520" y="1090" text-anchor="middle">Learners with Aspiration</text>
    <text class="body" x="520" y="1115" text-anchor="middle">Inspired and Believe in</text>
    <text class="body" x="520" y="1141" text-anchor="middle">pursuing great things</text>

    <!-- Schools -->
    <circle cx="836" cy="1103" r="6" fill="var(--red)"/>
    <text class="school-name" x="848" y="1108">Harbourview School</text>
    <circle cx="836" cy="1129" r="6" fill="var(--red)"/>
    <text class="school-name" x="848" y="1134">Crestmoor Private School</text>
  </svg>
</div>
</body>
</html>
```